High end Coffee Roaster needs a Label design for new Blend

We are looking for a label design for a new blend called "Cold Brew Blend". It is a blend of coffee that we use for making cold brew coffee. The blend is sold as the whole bean and ground coffee in a bag as well as pre-brewed ready to drink in a bottle. We would like the label to be elegant but fun and It must include our logo. Please check out or website brightmilebeans.com or social media @brightmilebeans for information on our company and our coffees if you need more ideas on the kind of product we offer and our style.
Updates

Requirements
Must have
• Our Company Logo. Creative design.
Should not have
• This project should NOT be a corporate company logo, Please do NOT submit a design for a company logo this is a project for a Label. We already have a logo and we are looking for a design on a label. I have uploaded several examples of what we are looking for. Those examples are from other coffee companies who have cold brew. Those are examples only to give you a better idea of what im looking for. DO NOT COPY THEM.

```html
<!DOCTYPE html>
<html lang="en">
<head>
<meta charset="utf-8">
<title>Bright Mile Beans – Cold Brew Coffee Label</title>
<link rel="stylesheet" href="https://fonts.googleapis.com/css2?family=Cormorant+Garamond:ital,wght@0,600;1,600&display=swap">
<style>
  :root {
    --paper: #ffffff;
    --label-plum: #634149;
    --ink-white: #ffffff;
    --cube-cream: #faf0e6;
    --cube-pink: #f0cccb;
    --cube-orange: #e0825a;
    --cube-tan: #e4b066;
    --cube-shadow: #a27c6a;
  }
  * { margin: 0; padding: 0; box-sizing: border-box; }
  html, body {
    width: 866px;
    height: 1200px;
    overflow: hidden;
    background: var(--paper);
  }
  .canvas {
    position: relative;
    width: 866px;
    height: 1200px;
    background: var(--paper);
  }
  .label {
    position: absolute;
    left: 85px;
    top: 91px;
    width: 693px;
    height: 1019px;
    background: var(--label-plum);
  }
  .brand {
    position: absolute;
    left: 0;
    top: 250px;
    width: 100%;
    display: flex;
    flex-direction: column;
    align-items: center;
    color: var(--ink-white);
    font-family: "Cormorant Garamond", Georgia, serif;
    font-weight: 600;
    font-style: normal;
  }
  .brand-mark {
    width: 78px;
    height: 78px;
    border: 5px solid var(--ink-white);
    border-radius: 50%;
    margin-bottom: 34px;
    margin-top: -140px;
  }
  .brand-name {
    font-size: 58px;
    line-height: 1;
    letter-spacing: 1px;
    text-transform: uppercase;
  }
  .brand-sub {
    margin-top: 20px;
    font-size: 26px;
    line-height: 1;
    letter-spacing: 26px;
    padding-left: 26px;
    text-transform: uppercase;
  }
  .pattern-band {
    position: absolute;
    left: 0;
    top: 438px;
    width: 100%;
    height: 345px;
    background: linear-gradient(
      to bottom,
      var(--cube-pink) 0%,
      var(--cube-cream) 22%,
      var(--cube-cream) 55%,
      var(--cube-shadow) 66%,
      var(--cube-orange) 74%,
      var(--cube-tan) 100%
    );
  }
  .product-name {
    position: absolute;
    left: 0;
    top: 800px;
    width: 100%;
    text-align: center;
    color: var(--ink-white);
    font-family: "Cormorant Garamond", Georgia, serif;
    font-style: italic;
    font-weight: 600;
    font-size: 76px;
    line-height: 1.2;
  }
</style>
</head>
<body>
  <main class="canvas">
    <section class="label">
      <div class="brand">
        <div class="brand-mark"></div>
        <div class="brand-name">Bright Mile</div>
        <div class="brand-sub">Beans</div>
      </div>
      <div class="pattern-band" role="img" aria-label="Band of repeating isometric cubes in cream, pink, orange and tan"></div>
      <h1 class="product-name">Cold Brew Coffee</h1>
    </section>
  </main>
</body>
</html>
```